Brisk Wire Services - Electrical

We need flyers for electrical services.
Areas of work include new builds, office fitouts, switchboard upgrades, installation of ceiling fans, powerpoint and downlight upgrades, home theatre and AV systems, all exterior and emergency work. Free quotes
We would like to see designs with the colour Red with a young and modern design. Licence No: 83146K must be included and call Leopold on 0418693027.

Colors
ec1f27

```html
<!DOCTYPE html>
<html lang="en">
<head>
<meta charset="utf-8">
<title>Brisk Wire Services – Electrical Flyer</title>
<link rel="stylesheet" href="https://fonts.googleapis.com/css2?family=Bebas+Neue&family=Roboto+Condensed:wght@500;700&family=Montserrat:wght@700;800;900&display=swap">
<style>
  :root {
    --brand-red: #ec1f27;
    --ink-black: #111111;
    --sheet-white: #ffffff;
    --soft-white: #f2f2f2;
    --badge-yellow: #fff200;
    --label-grey: #a9a9a9;
    --text-dark: #1b1b1b;
    --silver-light: #f4f4f4;
    --silver-dark: #9a9a9a;
  }
  * { margin: 0; padding: 0; box-sizing: border-box; }
  html, body { width: 903px; height: 1200px; overflow: hidden; background: #ffffff; }
  .flyer {
    position: relative;
    width: 903px;
    height: 1200px;
    overflow: hidden;
    background: var(--ink-black);
    font-family: "Roboto Condensed", "Arial Narrow", sans-serif;
  }
  .flyer__backdrop { position: absolute; inset: 0; }

  .headline {
    position: absolute;
    left: 44px;
    top: 28px;
    font-family: "Bebas Neue", "Oswald", sans-serif;
    line-height: 0.86;
    color: var(--sheet-white);
  }
  .headline__lead, .headline__tail { display: block; font-size: 80px; }
  .headline__trade { display: block; font-size: 126px; color: var(--brand-red); margin: 4px 0 6px; }

  .worker-photo {
    position: absolute;
    left: 22px;
    top: 365px;
    width: 462px;
    height: 620px;
    border-radius: 200px 200px 0 0;
    background: linear-gradient(180deg, #2f45b5 0%, #2a3ea8 55%, #8d8f98 80%, #5b5e66 100%);
  }

  .service-list {
    position: absolute;
    left: 452px;
    top: 655px;
    width: 440px;
  }
  .service-list__title {
    font-family: "Roboto Condensed", sans-serif;
    font-weight: 700;
    font-size: 38px;
    color: var(--label-grey);
    margin: 0 0 10px 41px;
    letter-spacing: 0.2px;
  }
  .service-list__items { list-style: none; }
  .service-item {
    display: flex;
    align-items: center;
    height: 48.3px;
    font-weight: 500;
    font-size: 28px;
    color: var(--text-dark);
    letter-spacing: -0.3px;
  }
  .service-item__icon { width: 28px; height: 28px; margin-right: 17px; flex: none; }

  .call-bar {
    position: absolute;
    left: 329px;
    top: 999px;
    width: 569px;
    height: 53px;
    background: var(--brand-red);
    color: var(--badge-yellow);
    font-family: "Montserrat", sans-serif;
    font-weight: 900;
    font-size: 47px;
    line-height: 53px;
    text-align: center;
    letter-spacing: 0.5px;
  }
  .call-number {
    position: absolute;
    left: 329px;
    top: 1062px;
    width: 569px;
    text-align: center;
    font-family: "Montserrat", sans-serif;
    font-weight: 800;
    font-size: 70px;
    line-height: 1;
    color: var(--ink-black);
    letter-spacing: -1px;
  }
  .licence {
    position: absolute;
    right: 33px;
    top: 1145px;
    text-align: right;
    font-family: "Montserrat", sans-serif;
    font-weight: 700;
    font-size: 11px;
    line-height: 15px;
    color: var(--ink-black);
  }
  .badge { position: absolute; }
  .badge text { font-family: "Bebas Neue", "Oswald", sans-serif; }
</style>
</head>
<body>
<main class="flyer">
  <svg class="flyer__backdrop" width="903" height="1200" viewBox="0 0 903 1200" aria-hidden="true">
    <rect width="903" height="1200" fill="var(--ink-black)"/>
    <polygon points="0,856 0,803 258,372 903,103 903,654 647,530" fill="var(--brand-red)"/>
    <polygon points="0,856 647,530 903,654 903,1200 0,1200" fill="var(--sheet-white)"/>
    <polygon points="0,856 647,530 903,654 903,1200 0,1200" fill="url(#sheetShade)"/>
    <defs>
      <linearGradient id="sheetShade" x1="0" y1="0" x2="0" y2="1">
        <stop offset="0" stop-color="#e9e9e9"/>
        <stop offset="1" stop-color="#ffffff"/>
      </linearGradient>
      <linearGradient id="panelTone" x1="0" y1="0" x2="1" y2="1">
        <stop offset="0" stop-color="#e8e8e8"/>
        <stop offset="0.6" stop-color="#cfd3d6"/>
        <stop offset="1" stop-color="#6c8aa0"/>
      </linearGradient>
    </defs>
    <polygon points="467,416 903,160 903,654 647,530" fill="url(#panelTone)" role="img" aria-label="Close-up of a hand testing wiring in a switchboard with circuit breakers"/>
  </svg>

  <h1 class="headline">
    <span class="headline__lead">Need an</span>
    <span class="headline__trade">Electrician</span>
    <span class="headline__tail">In your area</span>
  </h1>

  <div class="worker-photo" role="img" aria-label="Smiling electrician in blue overalls carrying a coil of cable and a multimeter"></div>

  <svg class="badge badge--guarantee" style="left:614px;top:52px" width="270" height="262" viewBox="0 0 270 262" aria-label="100% satisfaction guaranteed, get a free quote">
    <defs>
      <linearGradient id="ringSilverTop" x1="0" y1="0" x2="1" y2="1">
        <stop offset="0" stop-color="var(--silver-light)"/>
        <stop offset="0.5" stop-color="var(--silver-dark)"/>
        <stop offset="1" stop-color="var(--silver-light)"/>
      </linearGradient>
    </defs>
    <circle cx="133" cy="131" r="128" fill="url(#ringSilverTop)"/>
    <circle cx="133" cy="131" r="114" fill="var(--badge-yellow)"/>
    <text x="133" y="103" text-anchor="middle" font-size="86" fill="var(--brand-red)">100%</text>
    <text x="133" y="150" text-anchor="middle" font-size="40" fill="var(--ink-black)">SATISFACTION</text>
    <text x="133" y="188" text-anchor="middle" font-size="40" fill="var(--ink-black)">GUARANTEED</text>
    <polygon points="20,198 252,198 240,237 32,237" fill="var(--brand-red)"/>
    <text x="136" y="230" text-anchor="middle" font-size="34" fill="var(--sheet-white)">GET A FREE QUOTE</text>
  </svg>

  <section class="service-list">
    <h2 class="service-list__title">AREAS OF WORK</h2>
    <ul class="service-list__items">
      <li class="service-item">
        <svg class="service-item__icon" viewBox="0 0 28 28" aria-hidden="true"><polygon points="14,3 27,14 23,14 23,26 17,26 17,18 11,18 11,26 5,26 5,14 1,14" fill="var(--brand-red)"/></svg>
        New Builds, Office Fitouts
      </li>
      <li class="service-item">
        <svg class="service-item__icon" viewBox="0 0 28 28" aria-hidden="true"><rect x="3" y="3" width="22" height="22" rx="2" fill="var(--brand-red)"/><circle cx="9" cy="9" r="2.5" fill="#fff"/><circle cx="19" cy="9" r="2.5" fill="#fff"/><circle cx="9" cy="19" r="2.5" fill="#fff"/><circle cx="19" cy="19" r="2.5" fill="#fff"/></svg>
        Switchboard Upgrades
      </li>
      <li class="service-item">
        <svg class="service-item__icon" viewBox="0 0 28 28" aria-hidden="true"><g fill="var(--brand-red)"><circle cx="14" cy="15" r="3.5"/><ellipse cx="14" cy="6" rx="4" ry="6"/><ellipse cx="6" cy="20" rx="6" ry="4" transform="rotate(-30 6 20)"/><ellipse cx="22" cy="20" rx="6" ry="4" transform="rotate(30 22 20)"/></g></svg>
        Installation of Ceiling Fans
      </li>
      <li class="service-item">
        <svg class="service-item__icon" viewBox="0 0 28 28" aria-hidden="true"><g fill="var(--brand-red)"><circle cx="14" cy="12" r="7"/><rect x="10.5" y="18" width="7" height="6" rx="1"/><rect x="13" y="0" width="2" height="3"/><rect x="0" y="11" width="3" height="2"/><rect x="25" y="11" width="3" height="2"/><rect x="3" y="3" width="3" height="2" transform="rotate(45 4.5 4)"/><rect x="22" y="3" width="3" height="2" transform="rotate(-45 23.5 4)"/></g></svg>
        PowerPoint &amp; Downlight Upgrades
      </li>
      <li class="service-item">
        <svg class="service-item__icon" viewBox="0 0 28 28" aria-hidden="true"><g fill="var(--brand-red)"><rect x="0" y="5" width="5" height="19"/><rect x="23" y="5" width="5" height="19"/><rect x="7" y="5" width="14" height="11"/><rect x="9" y="19" width="10" height="5"/></g></svg>
        Home Theatre &amp; AV Systems
      </li>
      <li class="service-item">
        <svg class="service-item__icon" viewBox="0 0 28 28" aria-hidden="true"><circle cx="14" cy="14" r="11" fill="none" stroke="var(--brand-red)" stroke-width="3"/><g fill="var(--brand-red)"><rect x="8" y="10" width="9" height="8" rx="2"/><rect x="17" y="11" width="6" height="2"/><rect x="17" y="15" width="6" height="2"/><rect x="2" y="13" width="6" height="2"/></g></svg>
        All Emergency Work
      </li>
    </ul>
  </section>

  <svg class="badge badge--discount" style="left:46px;top:902px" width="280" height="280" viewBox="0 0 280 280" aria-label="20% discount to pensioners">
    <defs>
      <linearGradient id="ringSilverBottom" x1="0" y1="0" x2="1" y2="1">
        <stop offset="0" stop-color="var(--silver-light)"/>
        <stop offset="0.5" stop-color="var(--silver-dark)"/>
        <stop offset="1" stop-color="var(--silver-light)"/>
      </linearGradient>
    </defs>
    <circle cx="140" cy="140" r="136" fill="url(#ringSilverBottom)"/>
    <circle cx="140" cy="140" r="122" fill="var(--badge-yellow)"/>
    <text x="140" y="136" text-anchor="middle" font-size="112" fill="var(--brand-red)">20%</text>
    <text x="140" y="184" text-anchor="middle" font-size="44" fill="var(--ink-black)">DISCOUNT TO</text>
    <polygon points="20,196 260,196 242,244 38,244" fill="var(--brand-red)"/>
    <text x="140" y="237" text-anchor="middle" font-size="44" fill="var(--sheet-white)">PENSIONERS</text>
  </svg>

  <div class="call-bar">CALL LEOPOLD</div>
  <div class="call-number">0418 693 027</div>
  <p class="licence">BRISK WIRE SERVICES<br>LICENCE NO: 83146K</p>
</main>
</body>
</html>
```